Brochure Design Project

I have attached files of a brochure we had done several years ago that needs to be updated. We no longer have a mechanical division, which is what most of that brochure was used for so we need a new updated one. I am sharing it because we want to transfer over some of the other wording to create a new brochure. I also attached an example of a one page flier that was made just to give you some more ideas, as well as photos of some of our clients. As far as contacts to list (shown under Key Personnel on the example) the following need to be listed on the new brochure as listed on the previous: Wade Pollard, Marcus Feldtrane, and Emilio Vance. We need to add 5 additional to the contacts. They are: Grant Whitlock - Project Manager - grantwhitlock@dravelbuild.com - (317) 555-0192 ext. 106 (765) 555-0134 cell Tony Mallard - Estimator/Project Management Assistance - tonymallard@dravelbuild.com - (317) 555-0192 ext 117 - (765) 555-0178 cell Paul Dempsey - Project Manager - pauldempsey@dravelbuild.com - (317) 555-0192 ext 116 (765) 555-0121 Ray Tolliver - Project Manager - raytolliver@dravelbuild.com - (317) 555-0192 ext. 104 (765) 555-0156 Kevin Aldous - Facility Maintenance Manager - kevinaldous@dravelbuild.com - (317) 555-0192 ext 109 (317) 555-0147 cell
The list of services we provide can be seen on our website and need to be included on the brochure. http://dravelbuild.com/index.php/what-we-do/what-we-do-2

```html
<!DOCTYPE html>
<html lang="en">
<head>
<meta charset="utf-8">
<title>Dravel Build Services – Brochure</title>
<link rel="stylesheet" href="https://fonts.googleapis.com/css2?family=Arimo:wght@400;700&family=Saira+Semi+Condensed:wght@400;600&family=Michroma&display=swap">
<style>
:root{
  --ink:#231f20;
  --blue:#6682ad;
  --blue-deep:#47699e;
  --mist:#e7e9ed;
  --paper:#ffffff;
  --text:#2a2a2a;
  --dot:#7b93b8;
}
*{box-sizing:border-box;margin:0;padding:0}
html,body{width:959px;height:1200px;overflow:hidden;background:var(--paper)}
.page{position:relative;width:959px;height:1200px;overflow:hidden;background:var(--paper);
  font-family:'Saira Semi Condensed',sans-serif;color:var(--text);font-size:11px;line-height:1.3}
.abs{position:absolute}
.title-bar{position:absolute;background:var(--ink);color:#fff;font:700 17px/1 'Arimo',sans-serif;
  display:flex;align-items:center;padding-left:48px;white-space:nowrap;
  clip-path:polygon(0 0,100% 0,calc(100% - 16px) 100%,0 100%)}
.title-bar.slant-both{clip-path:polygon(16px 0,100% 0,calc(100% - 16px) 100%,0 100%);padding-left:30px}
.bullets{list-style:none}
.bullets li{position:relative;padding-left:12px}
.bullets li::before{content:"";position:absolute;left:2px;top:.55em;width:4px;height:4px;border-radius:50%;background:var(--dot)}
.band-blue{position:absolute;left:0;top:409px;width:800px;height:396px;background:var(--blue);
  clip-path:polygon(0 0,100% 0,749px 100%,0 100%)}
.band-mist{position:absolute;left:0;top:805px;width:959px;height:285px;background:var(--mist)}
.col-head{font:700 12.5px/1.25 'Arimo',sans-serif;color:var(--blue-deep);margin-bottom:3px}
.web-bar{position:absolute;background:var(--ink);color:#fff;font:400 13px/1 'Michroma',sans-serif;
  letter-spacing:1px;display:flex;align-items:center;padding-left:44px}
.brand-name{font:700 30px/1 'Arimo',sans-serif;color:var(--blue-deep);display:flex;align-items:center;gap:8px}
.brand-name .mark{width:14px;height:14px;background:var(--blue-deep)}
.tagline{font:700 27px/1.3 'Arimo',sans-serif;color:var(--ink);text-align:right}
.team-grid{position:absolute;left:50px;top:488px;width:510px;display:grid;grid-template-columns:255px 255px;row-gap:14px;color:#fff}
.person .name{font:700 12px/1.3 'Arimo',sans-serif}
.person .role{font-weight:400}
.person .line{font-size:10.5px;line-height:14px}
.clients{position:absolute;left:183px;top:1095px;width:740px;height:46px;display:flex;align-items:center;justify-content:space-between}
.client{font:600 9.5px/1.1 'Saira Semi Condensed',sans-serif;color:var(--blue-deep);text-align:center;width:56px}
.footer-blue{position:absolute;left:0;top:1151px;width:959px;height:49px;background:var(--blue)}
.footer-dark{position:absolute;left:566px;top:1151px;width:393px;height:49px;background:var(--ink);
  clip-path:polygon(22px 0,100% 0,100% 100%,0 100%)}
.footer-text{position:absolute;left:48px;top:1168px;color:#fff;font-size:11.5px}
.footer-web{position:absolute;left:612px;top:1164px;color:#fff;font:400 16px/1 'Michroma',sans-serif;letter-spacing:1.5px}
</style>
</head>
<body>
<div class="page">

  <!-- Renovation -->
  <div class="title-bar" style="left:0;top:36px;width:256px;height:28px">Renovation Services</div>
  <p class="abs" style="left:48px;top:76px;width:262px;font-size:10.5px;line-height:14.3px">From national chain Re-Image Programs to single-office remodeling projects, Dravel Build Services Inc. is dedicated to providing 100% customer satisfaction. Our highly skilled and dedicated team works with you and your company to develop a unique and effective plan to make your project a success.</p>
  <ul class="bullets abs" style="left:48px;top:178px;width:220px;font-size:10.5px;line-height:15px">
    <li>Restaurants</li><li>Retailers</li><li>Medical Facilities/Hospitals</li><li>Tenant Improvement Projects</li>
    <li>LL/Tenant White Box Projects</li><li>Relocations</li><li>Expansions or Downsizing</li>
    <li>Interior and Exterior Renovations</li><li>Store Closures</li><li>Open Remodels</li>
    <li>Fixture and Casework Replacements and/or Resets</li><li>National Rollouts and/or Upgrades</li>
  </ul>

  <svg class="abs" style="left:0;top:0" width="959" height="409" role="img" aria-label="Photographs of completed storefront renovations">
    <defs>
      <linearGradient id="shopA" x1="0" y1="0" x2="0" y2="1"><stop offset="0" stop-color="#b9c6d6"/><stop offset=".55" stop-color="#8d8477"/><stop offset="1" stop-color="#6e6d6c"/></linearGradient>
      <linearGradient id="shopB" x1="0" y1="0" x2="0" y2="1"><stop offset="0" stop-color="#c9d2de"/><stop offset=".6" stop-color="#9a7c63"/><stop offset="1" stop-color="#7a7b7c"/></linearGradient>
    </defs>
    <polygon points="361,0 511,0 493,88 340,88" fill="url(#shopA)"/>
    <polygon points="339,93 492,93 474,184 318,184" fill="url(#shopB)"/>
    <polygon points="317,189 473,189 450,304 290,304" fill="url(#shopA)"/>
    <polygon points="288,309 449,309 429,409 265,409" fill="url(#shopB)"/>
  </svg>

  <!-- Facility -->
  <div class="title-bar slant-both" style="left:516px;top:32px;width:324px;height:28px">Facility Repair &amp; Maintenance</div>
  <p class="abs" style="left:528px;top:70px;width:388px;font-size:10.5px;line-height:14.4px;text-align:center">Dravel Build Services Inc. provides all facets of facility repair and maintenance for a wide variety of nationwide retailers, restaurants, offices, and other commercial clients. We can handle anything from planned maintenance to 24/7 emergency on-call services. We understand how important it is to keep your business operational, so we work when our customers need us!</p>
  <ul class="bullets abs" style="left:524px;top:158px;width:230px;font-size:10.5px;line-height:14.5px">
    <li>General Building Repairs/Maintenance</li><li>24/7 On-Call Technicians</li><li>Trim Carpentry</li>
    <li>Casework Repair and Installation</li><li>Framing, Hanging, and Drywall Finishing and Repairs</li>
    <li>Painting and Wall Coverings</li><li>Flooring Including Wood, Carpeting, VCT, Tile, Concrete, etc.</li>
    <li>Acoustical Ceilings</li><li>Welding, Fencing and Gates</li><li>Doors, Hardware and Locks</li>
    <li>Plumbing, Drain and Sewer Services</li><li>Electrical and Lighting</li>
    <li>Masonry, Concrete and Asphalt</li><li>Roof Maintenance and Gutters</li>
  </ul>
  <ul class="bullets abs" style="left:760px;top:158px;width:170px;font-size:10.5px;line-height:14.5px">
    <li>Caulking, Leak Repairs and Waterproofing</li><li>Vandalism and Graffiti Removal</li>
    <li>Board-Ups and Break-In Repairs</li><li>Signage Installation and Repairs</li>
    <li>Facility Site Inspections/Audits</li><li>Fabrication Shop for Custom Metal and Wood Projects</li>
    <li>FF&amp;E Storage, Delivery, Set-up, and Removal Services</li><li>Demolition</li>
  </ul>
  <div class="web-bar" style="left:689px;top:374px;width:270px;height:27px;clip-path:polygon(10px 0,100% 0,100% 100%,0 100%)">www.dravelbuild.com</div>

  <!-- Team -->
  <div class="band-blue"></div>
  <div class="title-bar" style="left:0;top:442px;width:420px;height:28px">Our Team at Dravel Build Services, Inc.</div>
  <div class="team-grid">
    <div class="person"><div class="name">Wade Pollard <span class="role">- President</span></div><div class="line">wadepollard@dravelbuild.com</div><div class="line">(317) 555-0192</div></div>
    <div class="person"><div class="name">Marcus Feldtrane <span class="role">- CEO</span></div><div class="line">marcusfeldtrane@dravelbuild.com</div><div class="line">(317) 555-0192</div></div>
    <div class="person"><div class="name">Emilio Vance <span class="role">- Vice President - Dallas</span></div><div class="line">emiliovance@dravelbuild.com</div><div class="line">(317) 555-0192</div></div>
    <div class="person"><div class="name">Grant Whitlock <span class="role">- Project Manager</span></div><div class="line">grantwhitlock@dravelbuild.com</div><div class="line">(317) 555-0192 ext. 106 &nbsp;|&nbsp; (765) 555-0134 cell</div></div>
    <div class="person"><div class="name">Tony Mallard <span class="role">- Estimator/PM Assistance</span></div><div class="line">tonymallard@dravelbuild.com</div><div class="line">(317) 555-0192 ext. 117 &nbsp;|&nbsp; (765) 555-0178 cell</div></div>
    <div class="person"><div class="name">Paul Dempsey <span class="role">- Project Manager</span></div><div class="line">pauldempsey@dravelbuild.com</div><div class="line">(317) 555-0192 ext. 116 &nbsp;|&nbsp; (765) 555-0121 cell</div></div>
    <div class="person"><div class="name">Ray Tolliver <span class="role">- Project Manager</span></div><div class="line">raytolliver@dravelbuild.com</div><div class="line">(317) 555-0192 ext. 104 &nbsp;|&nbsp; (765) 555-0156 cell</div></div>
    <div class="person"><div class="name">Kevin Aldous <span class="role">- Facility Maint. Manager</span></div><div class="line">kevinaldous@dravelbuild.com</div><div class="line">(317) 555-0192 ext. 109 &nbsp;|&nbsp; (317) 555-0147 cell</div></div>
  </div>

  <svg class="abs" style="left:0;top:409px" width="959" height="396" role="img" aria-label="Photographs of finished commercial building exteriors">
    <defs>
      <linearGradient id="shopC" x1="0" y1="0" x2="0" y2="1"><stop offset="0" stop-color="#c3cedb"/><stop offset=".55" stop-color="#8e7f70"/><stop offset="1" stop-color="#757473"/></linearGradient>
    </defs>
    <polygon points="639,0 799,0 788,85 622,85" fill="url(#shopC)"/>
    <polygon points="621,90 788,90 775,191 602,191" fill="url(#shopC)"/>
    <polygon points="601,196 774,196 762,294 582,294" fill="url(#shopC)"/>
    <polygon points="581,299 761,299 749,396 562,396" fill="url(#shopC)"/>
  </svg>

  <div class="abs" style="left:806px;top:626px;width:140px">
    <div class="brand-name"><span class="mark"></span>Dravel</div>
  </div>
  <div class="tagline abs" style="right:28px;top:700px;width:180px">Delivering beyond expectation</div>

  <!-- Construction Management -->
  <div class="band-mist"></div>
  <div class="title-bar" style="left:0;top:848px;width:361px;height:28px">Construction Management</div>
  <p class="abs" style="left:50px;top:892px;width:335px;font-size:11px;line-height:15px">We specialize in Restaurants, Retail, Medical and Commercial/Office Construction. Our goal is to exceed your expectations in all the construction services we offer.</p>
  <div class="abs" style="left:414px;top:848px;width:145px;font-size:11px;line-height:17px">
    <div class="col-head">New and Ground-up Construction</div>
    <ul class="bullets"><li>Shell Construction/ Free-Standing</li><li>Multi-Tenant Centers</li><li>Land Development</li><li>Design/Build Services</li></ul>
  </div>
  <div class="abs" style="left:566px;top:848px;width:150px;font-size:11px;line-height:17px">
    <div class="col-head">Interior Finish-Outs</div>
    <ul class="bullets"><li>In-line Tenant Spaces</li><li>Mall Spaces</li><li>Free-Standing Buildings</li><li>Office Interiors</li><li>Kiosks</li></ul>
  </div>
  <div class="abs" style="left:721px;top:848px;width:210px;font-size:11px;line-height:17px">
    <div class="col-head">Renovations</div>
    <ul class="bullets"><li>Open or Closed Remodels</li><li>Re-branding/Re-imaging Programs</li><li>Fixture Installations</li><li>Building Additions or Downsizing</li><li>Re-locations</li><li>Temporary Facilities</li></ul>
  </div>

  <!-- Clients -->
  <div class="title-bar" style="left:0;top:1106px;width:173px;height:28px;padding-left:44px">Our Clients</div>
  <div class="clients">
    <span class="client">Jolly Burgers</span><span class="client">Penny Grove</span><span class="client">Mesa Cantina</span>
    <span class="client">Bunhaus</span><span class="client">Tilestack Pizza</span><span class="client">Wing Barn</span>
    <span class="client">Eight Ten Salons</span><span class="client">Home Coin</span><span class="client">Taco Lantern</span>
    <span class="client">Burrito Loft</span><span class="client">Harbor Roast</span><span class="client">Six Pals</span>
  </div>

  <!-- Footer -->
  <div class="footer-blue"></div>
  <div class="footer-dark"></div>
  <div class="footer-text">2210 N. County Road 7, Millbrook, IN 46099 &nbsp;|&nbsp; Phone: (317) 555-0192 &nbsp;|&nbsp; Fax: (317) 555-0110</div>
  <div class="footer-web">www.dravelbuild.com</div>

</div>
</body>
</html>
```